Design Business Cards for Dr. Pelican

I am looking for business cards for my new educational toy business. It is important the business cards are fun and exciting.

Check the attached PDF for potential business card ideas. I have also attached the logo in PNG and JPG. Feel free to cut this up and use just the monkey or just the text etc.

On the business card we would like:

- Person name
- Logo
- Title
- Website
- Email
- Phone

Most importantly, we are looking for something funky, cool and different!

```html
<!DOCTYPE html>
<html lang="en">
<head>
<meta charset="utf-8">
<title>Dr. Pelican – Business Cards</title>
<link rel="stylesheet" href="https://fonts.googleapis.com/css2?family=Arimo:wght@400;700&display=swap">
<style>
  :root {
    --page: #d9d9d9;
    --card: #1c1c1d;
    --card-edge: #111112;
    --pink: #e94f70;
    --grey: #9a9a9a;
    --glow-core: #f2b52a;
    --glow-warm: #d9781c;
    --ray-pink: #e94f70;
    --ray-green: #4fbf8c;
    --ray-blue: #4f7ad6;
    --brand-text: #f2b52a;
  }
  * { box-sizing: border-box; margin: 0; padding: 0; }
  html, body { width: 1200px; height: 937px; overflow: hidden; }
  body {
    background: var(--page);
    font-family: "Arimo", Arial, sans-serif;
    display: flex;
    flex-direction: column;
    align-items: center;
    justify-content: center;
    gap: 40px;
  }
  .card {
    position: relative;
    width: 720px;
    height: 411px;
    background: var(--card);
    border: 1px solid var(--card-edge);
    overflow: hidden;
  }

  /* Front */
  .front-rays {
    position: absolute;
    left: 210px; top: 0;
    width: 300px; height: 300px;
    background: linear-gradient(90deg,
      rgba(233,79,112,0) 0%, var(--ray-pink) 22%, var(--glow-core) 42%,
      var(--glow-core) 55%, var(--ray-green) 72%, var(--ray-blue) 86%, rgba(79,122,214,0) 100%);
    -webkit-mask-image: linear-gradient(180deg, rgba(0,0,0,.7) 0%, rgba(0,0,0,.45) 35%, rgba(0,0,0,0) 100%);
            mask-image: linear-gradient(180deg, rgba(0,0,0,.7) 0%, rgba(0,0,0,.45) 35%, rgba(0,0,0,0) 100%);
    opacity: .7;
  }
  .front-glow {
    position: absolute;
    left: 220px; top: 20px;
    width: 280px; height: 310px;
    background: radial-gradient(closest-side, var(--glow-core) 0%, rgba(217,120,28,.8) 45%, rgba(28,28,29,0) 100%);
    opacity: .8;
  }
  .front-mark {
    position: absolute;
    left: 50%; top: 70px;
    width: 170px; height: 170px;
    margin-left: -85px;
    border-radius: 50%;
    background: var(--pink);
  }
  .front-name {
    position: absolute;
    left: 0; right: 0; top: 262px;
    text-align: center;
    font-weight: 700;
    font-size: 30px;
    color: var(--brand-text);
  }

  /* Back */
  .back-mark {
    position: absolute;
    left: 54px; top: 104px;
    width: 92px; height: 92px;
    border-radius: 50%;
    background: var(--pink);
  }
  .holder {
    position: absolute;
    left: 190px; top: 88px;
  }
  .holder-name {
    font-size: 22px;
    letter-spacing: .5px;
    color: var(--pink);
    text-transform: uppercase;
  }
  .holder-title {
    font-size: 15px;
    color: var(--grey);
    margin-top: 2px;
  }
  .domain-band {
    position: absolute;
    left: 150px; top: 140px;
    width: 480px; height: 110px;
    background: radial-gradient(closest-side, var(--glow-core) 0%, rgba(217,120,28,.75) 50%, rgba(28,28,29,0) 100%);
    opacity: .8;
  }
  .domain {
    position: absolute;
    left: 188px; top: 168px;
    font-weight: 700;
    font-size: 44px;
    color: var(--brand-text);
  }
  .contact {
    position: absolute;
    right: 28px; bottom: 26px;
    list-style: none;
    text-align: right;
    color: var(--pink);
    font-size: 15px;
    line-height: 24px;
  }
  .contact li { display: flex; align-items: center; justify-content: flex-end; gap: 10px; }
  .contact svg { width: 14px; height: 14px; fill: none; stroke: var(--pink); stroke-width: 2; }
</style>
</head>
<body>

  <section class="card card-front">
    <div class="front-rays" role="img" aria-label="Soft rainbow light rays falling from the top edge"></div>
    <div class="front-glow" role="img" aria-label="Soft warm light glow behind the brand mark"></div>
    <div class="front-mark"></div>
    <div class="front-name">Dr. Pelican</div>
  </section>

  <section class="card card-back">
    <div class="back-mark"></div>
    <div class="holder">
      <p class="holder-name">Lena Marlow</p>
      <p class="holder-title">designer</p>
    </div>
    <div class="domain-band" role="img" aria-label="Soft warm light streak behind the web address"></div>
    <div class="domain">Dr.Pelican.com.au</div>
    <ul class="contact">
      <li>(0142) 318 650
        <svg viewBox="0 0 16 16"><path d="M3 2h3l1 4-2 1a8 8 0 0 0 4 4l1-2 4 1v3a1 1 0 0 1-1 1A12 12 0 0 1 2 3a1 1 0 0 1 1-1z"/></svg>
      </li>
      <li>name@drpelican.com.au
        <svg viewBox="0 0 16 16"><rect x="1.5" y="3.5" width="13" height="9"/><path d="M1.5 3.5l6.5 5 6.5-5"/></svg>
      </li>
      <li>www.drpelican.com.au
        <svg viewBox="0 0 16 16"><circle cx="8" cy="8" r="6.5"/><path d="M1.5 8h13M8 1.5c3 3.5 3 9.5 0 13M8 1.5c-3 3.5-3 9.5 0 13"/></svg>
      </li>
    </ul>
  </section>

</body>
</html>
```